project - Kestra Nook

Dear designers, I'm Looking for an appealing new business card design to represent us for our new e-cigarette store: The KestrA Nook. Knowledgeable and friendly staff we aim for superior customer service with a positive atmosphere. Classic feel with modern touch is what we are aiming for . Lime green font and grey back round is the original color scheme but we are flexible and open to suggestions. I added some doodles to show you where my mind is at. address: 4308 87 Ave NW Edmonton, AB (inside the hollin trade hall)web: thekestranook.com email: info@thekestranook.com phone : 587.555.0148 Thanks and am looking forward to seeing your creative , fresh and innovative designs.
Good luck everybody!
Jonas
lime green and charcoal grey please. thanks
Business
The KestrA Nook

```html
<!DOCTYPE html>
<html lang="en">
<head>
<meta charset="utf-8">
<title>Kestra Nook – Business Card</title>
<link rel="stylesheet" href="https://fonts.googleapis.com/css2?family=Exo+2:wght@700;800&family=Open+Sans:wght@400;600&display=swap">
<style>
  :root {
    --lime: #3fae3a;
    --lime-light: #7ccc3c;
    --charcoal: #555759;
    --ink: #3a3b3d;
    --paper: #ffffff;
    --paper-shade: #e9eaea;
    --rim: #cfd1d1;
    --backdrop: #d9d6d1;
  }
  * { margin: 0; padding: 0; box-sizing: border-box; }
  html, body { width: 1200px; height: 899px; overflow: hidden; }
  body {
    background: var(--backdrop);
    font-family: "Open Sans", Arial, sans-serif;
    position: relative;
  }
  .card {
    position: absolute;
    top: 295px;
    width: 540px;
    height: 309px;
    border-radius: 26px;
    background: linear-gradient(160deg, var(--paper) 40%, var(--paper-shade) 100%);
    box-shadow: 0 6px 22px rgba(0,0,0,.18);
    overflow: hidden;
  }
  .card--front { left: 40px; }
  .card--back { left: 620px; display: flex; align-items: center; justify-content: center; }

  .wordmark {
    font-family: "Exo 2", Arial, sans-serif;
    font-weight: 800;
    color: var(--charcoal);
    line-height: .95;
    letter-spacing: 1px;
  }
  .card--front .wordmark {
    position: absolute;
    left: 34px;
    top: 62px;
    font-size: 56px;
  }
  .card--back .wordmark { font-size: 58px; margin-top: -10px; }

  .contact {
    position: absolute;
    left: 288px;
    top: 40px;
    width: 232px;
    color: var(--ink);
  }
  .contact__name {
    color: var(--lime);
    font-weight: 600;
    font-size: 16px;
    letter-spacing: 1px;
    text-transform: uppercase;
    line-height: 1.3;
  }
  .contact__title { font-size: 12px; margin-bottom: 12px; }
  .contact__address { font-size: 13px; line-height: 1.35; margin-bottom: 10px; }
  .contact__list { list-style: none; font-size: 10.5px; }
  .contact__list li { display: flex; align-items: center; gap: 8px; height: 16px; }
  .contact__list svg { width: 11px; height: 11px; fill: var(--lime); flex: none; }

  .swoosh { position: absolute; left: 0; bottom: 0; width: 540px; height: 66px; }
  .website {
    position: absolute;
    left: 120px;
    bottom: 12px;
    color: var(--paper);
    font-size: 11px;
    letter-spacing: 1.5px;
  }
</style>
</head>
<body>
  <article class="card card--front">
    <div class="wordmark">KESTRA<br>NOOK</div>

    <div class="contact">
      <p class="contact__name">Marek Dalton</p>
      <p class="contact__title">Managing Director</p>
      <p class="contact__address">4308 87 Ave NW<br>Edmonton, AB</p>
      <ul class="contact__list">
        <li><svg viewBox="0 0 12 12"><path d="M3 0h2l1 3-1.5 1.2a7 7 0 0 0 3.3 3.3L9 6l3 1v2c0 1.5-1 3-3 3A9 9 0 0 1 0 3c0-2 1.5-3 3-3z"/></svg>587.555.0148</li>
        <li><svg viewBox="0 0 12 12"><rect x="3" y="0" width="6" height="12" rx="1.2"/></svg>587.555.0148</li>
        <li><svg viewBox="0 0 12 12"><rect x="0" y="2" width="12" height="8" rx="1"/></svg>587.555.0148</li>
        <li><svg viewBox="0 0 12 12"><path d="M0 2h12v8H0z M0 2l6 4 6-4"/></svg>info@thekestranook.com</li>
        <li><svg viewBox="0 0 12 12"><circle cx="6" cy="6" r="6"/></svg>thekestranook.com</li>
      </ul>
    </div>

    <svg class="swoosh" viewBox="0 0 540 66" preserveAspectRatio="none" aria-hidden="true">
      <defs>
        <linearGradient id="swoosh-fill" x1="0" x2="1">
          <stop offset="0" stop-color="var(--lime)"/>
          <stop offset="1" stop-color="var(--lime-light)"/>
        </linearGradient>
      </defs>
      <path d="M0 20 Q270 2 540 30 L540 66 L0 66 Z" fill="var(--rim)"/>
      <path d="M0 27 Q270 10 540 38 L540 66 L0 66 Z" fill="url(#swoosh-fill)"/>
    </svg>
    <p class="website">www.thekestranook.com</p>
  </article>

  <article class="card card--back">
    <div class="wordmark">KESTRA NOOK</div>
  </article>
</body>
</html>
```